Update Business Card Design

I'm looking to update my business cards. Attached is a photo of the current design. I like the black side so that does not have to be update. The white side needs to be updated. I want the design to be modern and minimalistic.
I am a lawyer and my firm's website is www.brennoxlegalco.com (for reference).
My firm's logo has a horizontal version (which is on the black side of the card) and a vertical version (on the white side). I would prefer to keep the vertical version on the white side and horizontal version on the black side (the logo files are attached).

I am open to redesigning the black side also. I would like one side to have the horizontal logo and the other to have the vertical logo.

```html
<!DOCTYPE html>
<html lang="en">
<head>
<meta charset="utf-8">
<title>Brennox Legal Co — Business Card</title>
<link href="https://fonts.googleapis.com/css2?family=Tinos:wght@400;700&display=swap" rel="stylesheet">
<style>
  :root {
    --backdrop: #2b2c2e;
    --teal: #1ba3cf;
    --card-white: #f7f8f9;
    --card-black: #040506;
    --ink-light: #e9ecee;
    --ink-dark: #222;
    --mark-faint-light: #e2eff4;
    --mark-faint-dark: #0a1b21;
    --rule-dark: #3a3d40;
  }
  * { box-sizing: border-box; margin: 0; padding: 0; }
  html, body { width: 1200px; height: 900px; overflow: hidden; }
  body {
    background: var(--backdrop);
    font-family: "Tinos", "Times New Roman", serif;
    position: relative;
  }
  .card {
    position: absolute;
    left: 250px;
    width: 700px;
    height: 400px;
    overflow: hidden;
    box-shadow: 0 12px 30px rgba(0,0,0,.45);
  }
  .card--front { top: 30px; background: var(--card-white); }
  .card--back { top: 470px; background: var(--card-black); color: var(--ink-light); }

  .decor-disc {
    position: absolute;
    border-radius: 50%;
  }
  .card--front .decor-disc { width: 360px; height: 360px; right: -30px; top: -60px; background: var(--mark-faint-light); }
  .card--back .decor-disc { width: 380px; height: 380px; right: 40px; top: -90px; background: var(--mark-faint-dark); }

  .front-name {
    position: absolute;
    left: 60px; top: 200px;
    font-size: 58px;
    color: var(--teal);
    letter-spacing: 1px;
  }
  .front-rule {
    position: absolute;
    left: 60px; top: 292px;
    width: 360px; height: 1px;
    background: var(--teal);
  }
  .front-web {
    position: absolute;
    left: 60px; top: 306px;
    font-size: 17px;
    letter-spacing: 4px;
    color: var(--ink-dark);
  }

  .person { position: absolute; left: 50px; top: 58px; }
  .person-name {
    font-weight: 700; font-size: 22px; color: var(--teal);
    text-transform: uppercase; letter-spacing: .5px;
  }
  .person-title { font-size: 17px; margin-top: 4px; }

  .contact-list {
    position: absolute; left: 80px; top: 138px;
    list-style: none; font-size: 17px;
  }
  .contact-list li { display: flex; align-items: center; gap: 10px; height: 26px; }
  .contact-list svg { width: 16px; height: 16px; fill: none; stroke: var(--ink-light); stroke-width: 1.5; }
  .accent { color: var(--teal); }

  .back-rule {
    position: absolute; left: 80px; top: 290px;
    width: 380px; height: 1px; background: var(--rule-dark);
  }
  .brand {
    position: absolute; left: 80px; top: 308px;
    display: flex; align-items: center; gap: 16px;
  }
  .brand-dot { width: 46px; height: 46px; border-radius: 50%; background: var(--teal); }
  .brand-name { font-size: 34px; color: var(--teal); letter-spacing: 1px; }

  .address {
    position: absolute; right: 50px; top: 236px;
    text-align: right; font-size: 17px; line-height: 1.4;
  }
</style>
</head>
<body>
  <section class="card card--front">
    <div class="decor-disc"></div>
    <div class="front-name">BRENNOX LEGAL</div>
    <div class="front-rule"></div>
    <div class="front-web">www.BrennoxLegalCo.com</div>
  </section>

  <section class="card card--back">
    <div class="decor-disc"></div>
    <div class="person">
      <div class="person-name">Daniel Corwin</div>
      <div class="person-title">Founder | Attorney of Brennox Legal Co</div>
    </div>
    <ul class="contact-list">
      <li><svg viewBox="0 0 16 16"><rect x="4" y="1" width="8" height="14" rx="1.5"/></svg>310.555.0142</li>
      <li><svg viewBox="0 0 16 16"><path d="M3 2l3 0 1 3-2 1a8 8 0 0 0 5 5l1-2 3 1v3a1 1 0 0 1-1 1A12 12 0 0 1 2 3a1 1 0 0 1 1-1z"/></svg>877.555.0198</li>
      <li><svg viewBox="0 0 16 16"><rect x="2" y="6" width="12" height="7"/><rect x="4" y="2" width="8" height="4"/><line x1="5" y1="10" x2="11" y2="10"/></svg>310.555.0176</li>
      <li><svg viewBox="0 0 16 16"><rect x="1.5" y="3.5" width="13" height="9"/><path d="M1.5 3.5l6.5 5 6.5-5"/></svg>daniel@<span class="accent">BrennoxLegalCo</span>.com</li>
      <li><svg viewBox="0 0 16 16"><circle cx="8" cy="8" r="6.5"/><ellipse cx="8" cy="8" rx="3" ry="6.5"/><line x1="1.5" y1="8" x2="14.5" y2="8"/></svg>www.<span class="accent">BrennoxLegalCo</span>.com</li>
    </ul>
    <div class="back-rule"></div>
    <div class="brand">
      <div class="brand-dot"></div>
      <div class="brand-name">BRENNOX LEGAL CO</div>
    </div>
    <div class="address">318 Laurel Crest Avenue<br>Suite 410, Westbrook, CA 90000</div>
  </section>
</body>
</html>
```